Updated Business Card Re-design (Logo Provided)

I am needing to update our business cards for our practice, Bright Harbor Care. We are a personal injury and wellness practice. The final design should be elegant and classy, but a type of card people would want to keep. Any samples should only have Dr. Tarek Minouvel on the template.
Updates

Went on vacation/holiday

Need extra days to review

Target Market(s)

Personal Injury clients, wellness clients

Industry/Entity Type

Personal Injury, medical, wellness

Contact Information for Business Card

dr and practice name, offerings

Requirements
Must have
• Single sided, this will be printed on a transparent business card, no exceptions.

```html
<!DOCTYPE html>
<html lang="en">
<head>
<meta charset="utf-8">
<title>Bright Harbor Care — Business Card</title>
<link rel="stylesheet" href="https://fonts.googleapis.com/css2?family=Montserrat:wght@700&family=Arimo:wght@400;700&display=swap">
<style>
  :root {
    --page: #4b82ae;
    --frost-top: #d9dee3;
    --frost-bottom: #b9c2cb;
    --brand-blue: #1b7fc2;
    --deep-blue: #1672b3;
    --accent-orange: #ee9a2e;
    --ink: #2a2f36;
    --white: #ffffff;
  }
  html, body {
    margin: 0;
    width: 1200px;
    height: 800px;
    overflow: hidden;
    background: var(--page);
  }
  .business-card {
    position: absolute;
    left: 75px;
    top: 100px;
    width: 1050px;
    height: 600px;
    border-radius: 34px;
    overflow: hidden;
    box-shadow: 0 18px 40px rgba(10, 40, 70, 0.35);
    font-family: "Arimo", Arial, sans-serif;
  }
  .card-shapes {
    position: absolute;
    inset: 0;
  }
  .practice-name {
    position: absolute;
    left: 60px;
    top: 60px;
    margin: 0;
    font-family: "Montserrat", Arial, sans-serif;
    font-weight: 700;
    font-size: 58px;
    letter-spacing: -0.5px;
    color: var(--brand-blue);
  }
  .contact-list {
    position: absolute;
    margin: 0;
    padding: 0;
    list-style: none;
    font-size: 24px;
    color: var(--ink);
    line-height: 34px;
    white-space: nowrap;
  }
  .contact-list li {
    display: flex;
    align-items: flex-start;
    gap: 10px;
  }
  .contact-list svg {
    flex: none;
    width: 22px;
    height: 22px;
    margin-top: 6px;
    fill: var(--accent-orange);
  }
  .contact-phones { left: 60px; top: 200px; }
  .contact-online { left: 260px; top: 290px; }
  .contact-address { left: 60px; top: 380px; }
  .doctor-name {
    position: absolute;
    left: 630px;
    top: 312px;
    margin: 0;
    font-size: 40px;
    line-height: 48px;
    font-weight: 400;
    color: var(--white);
    letter-spacing: 0.5px;
    white-space: nowrap;
  }
  .service-list {
    position: absolute;
    left: 660px;
    top: 392px;
    margin: 0;
    padding: 0;
    list-style: none;
    font-size: 26px;
    line-height: 33px;
    color: var(--white);
    white-space: nowrap;
  }
  .service-list li::before {
    content: "•";
    margin-right: 8px;
  }
</style>
</head>
<body>
  <article class="business-card">
    <svg class="card-shapes" viewBox="0 0 1050 600" width="1050" height="600" aria-hidden="true">
      <defs>
        <linearGradient id="frost" x1="0" y1="0" x2="0.6" y2="1">
          <stop offset="0" stop-color="var(--frost-top)"/>
          <stop offset="1" stop-color="var(--frost-bottom)"/>
        </linearGradient>
      </defs>
      <rect class="frosted-base" width="1050" height="600" fill="url(#frost)"/>
      <path class="upper-accent" d="M760,0 C825,80 820,200 755,265 C792,190 792,80 735,0 Z" fill="var(--accent-orange)"/>
      <path class="blue-wave" d="M790,0 C860,110 830,250 700,300 L640,372 C600,440 610,530 650,600 L1050,600 L1050,0 Z" fill="var(--deep-blue)"/>
      <path class="lower-accent" d="M610,600 C575,510 590,420 650,385 C620,440 620,530 650,600 Z" fill="var(--accent-orange)"/>
      <path class="name-band" d="M600,300 L1050,300 L1050,372 L640,372 Q612,340 600,300 Z" fill="var(--accent-orange)"/>
    </svg>

    <h1 class="practice-name">Bright Harbor Care</h1>

    <ul class="contact-list contact-phones">
      <li><svg viewBox="0 0 24 24"><path d="M6.6 10.8a15 15 0 0 0 6.6 6.6l2.2-2.2a1 1 0 0 1 1-.25 11.4 11.4 0 0 0 3.6.57 1 1 0 0 1 1 1V20a1 1 0 0 1-1 1A17 17 0 0 1 3 4a1 1 0 0 1 1-1h3.5a1 1 0 0 1 1 1 11.4 11.4 0 0 0 .57 3.6 1 1 0 0 1-.25 1z"/></svg>555.014.2270</li>
      <li><svg viewBox="0 0 24 24"><path d="M7 1h10a2 2 0 0 1 2 2v18a2 2 0 0 1-2 2H7a2 2 0 0 1-2-2V3a2 2 0 0 1 2-2zm0 3v14h10V4zm5 15.5a1.2 1.2 0 1 0 0 2.4 1.2 1.2 0 0 0 0-2.4z"/></svg>555.014.3318</li>
    </ul>

    <ul class="contact-list contact-online">
      <li><svg viewBox="0 0 24 24"><path d="M2 5h20v14H2zm2 2v.5l8 5 8-5V7z"/></svg>hello@bhcare.example</li>
      <li><svg viewBox="0 0 24 24"><path d="M12 2a10 10 0 1 0 0 20 10 10 0 0 0 0-20zm6.9 6h-3a15 15 0 0 0-1.4-3.6A8 8 0 0 1 18.9 8zM12 4c.8 1.1 1.5 2.5 1.9 4h-3.8c.4-1.5 1.1-2.9 1.9-4zM4.3 14a8 8 0 0 1 0-4h3.4a16 16 0 0 0 0 4zm.8 2h3a15 15 0 0 0 1.4 3.6A8 8 0 0 1 5.1 16zm3-8h-3a8 8 0 0 1 4.4-3.6A15 15 0 0 0 8.1 8zM12 20c-.8-1.1-1.5-2.5-1.9-4h3.8c-.4 1.5-1.1 2.9-1.9 4zm2.3-6H9.7a14 14 0 0 1 0-4h4.6a14 14 0 0 1 0 4zm.2 5.6a15 15 0 0 0 1.4-3.6h3a8 8 0 0 1-4.4 3.6zm1.8-5.6a16 16 0 0 0 0-4h3.4a8 8 0 0 1 0 4z"/></svg>bhcare.example</li>
    </ul>

    <ul class="contact-list contact-address">
      <li><svg viewBox="0 0 24 24"><path d="M12 2a7 7 0 0 0-7 7c0 5.2 7 13 7 13s7-7.8 7-13a7 7 0 0 0-7-7zm0 9.5A2.5 2.5 0 1 1 12 6.5a2.5 2.5 0 0 1 0 5z"/></svg><span>4820 Lantern Road, Suite 12<br>Fairview, GA 30000</span></li>
    </ul>

    <h2 class="doctor-name">Dr. Tarek Minouvel</h2>

    <ul class="service-list">
      <li>Auto Accident Care</li>
      <li>Primary Care</li>
      <li>Medical Weight Loss</li>
      <li>Physical Therapy</li>
      <li>Chiropractic Care</li>
    </ul>
  </article>
</body>
</html>
```